Presentation Folder

We are looking for a presentation folder design that will allow us to bring our proposals/quotes to clients and leave with them. The front cover should have our logo as well as show some of the products we sell: IT Networking equipment, WiFi, Servers/Storage.
Inside flap has an area for our business cards.

Target Market(s)

Mid Sized Businesses and Private Education. Business to Business. IT Directors. Ages 30 to 50. College Educated. Southern California

Industry/Entity Type

Business

Logo Text

Requirements
Must have
• Our Logo
Complimentary color schemes to our logo.
Should be Professional.

```html
<!DOCTYPE html>
<html lang="en">
<head>
<meta charset="utf-8">
<title>Halvern IT Presentation Folder</title>
<link href="https://fonts.googleapis.com/css2?family=Raleway:wght@300;400;600&display=swap" rel="stylesheet">
<style>
  :root{
    --bg:#e4e4e4;
    --paper:#ffffff;
    --paper-shade:#f1f1f1;
    --inner-grey:#d9d9d9;
    --orange:#e8792a;
    --orange-deep:#d4531f;
    --blue:#0aafdb;
    --blue-light:#3cc4e8;
    --teal:#1585a8;
    --charcoal:#3a3a3a;
    --card:#2b2b2b;
    --text-grey:#7a7a7a;
    --pocket-text:#c9c9c9;
  }
  *{box-sizing:border-box;margin:0;padding:0}
  html,body{width:1200px;height:847px;overflow:hidden}
  body{
    background:radial-gradient(ellipse at 50% 45%, #f4f4f4 0%, var(--bg) 70%, #cfcfcf 100%);
    font-family:"Raleway", Arial, sans-serif;
    position:relative;
  }
  .panel{
    position:absolute;top:250px;width:260px;height:347px;overflow:hidden;
    box-shadow:0 8px 22px rgba(0,0,0,.18);
  }
  .panel svg.art{position:absolute;inset:0}

  /* Front cover */
  .front-cover{left:40px;background:var(--paper)}
  .front-cover .wordmark{
    position:absolute;left:40px;top:126px;
    font-weight:300;font-size:32px;letter-spacing:1px;color:var(--text-grey);
  }
  .product-band{
    position:absolute;left:0;top:180px;width:100%;height:44px;
    background:linear-gradient(#d6d6d6,#c4c4c4);
    border-top:3px solid var(--teal);border-bottom:3px solid var(--teal);
  }
  .product-band .products{
    position:absolute;left:10px;right:10px;top:2px;bottom:2px;
    background:linear-gradient(90deg,#9a9ea4 0%,#e8e6e0 45%,#6f8a6a 85%,#c4c4c4 100%);
    border-radius:3px;opacity:.85;
  }

  /* Inside spread */
  .inside-left{left:340px;background:linear-gradient(110deg,var(--paper) 55%,var(--paper-shade))}
  .inside-right{left:600px;background:linear-gradient(90deg,#c9c9c9,var(--inner-grey) 20%,#e2e2e2)}
  .pocket{position:absolute;left:0;bottom:0;width:100%;height:80px}
  .pocket-left{background:var(--charcoal)}
  .pocket-left .wordmark{
    position:absolute;left:26px;top:22px;
    font-weight:300;font-size:30px;letter-spacing:1px;color:var(--pocket-text);
  }
  .pocket-right{background:var(--orange)}
  .business-card{
    position:absolute;left:44px;top:14px;width:96px;height:54px;
    background:var(--card);color:#fff;padding:6px 7px;
    border-top:3px solid #111;
  }
  .business-card .card-name{font-weight:300;font-size:11px;letter-spacing:.5px;color:#e6e6e6}
  .business-card .card-lines{font-size:5px;line-height:6.5px;margin-top:3px;color:#d0d0d0}

  /* Back cover */
  .back-cover{left:900px;background:var(--blue)}
  .back-band{
    position:absolute;left:0;top:268px;width:100%;height:42px;background:var(--paper);
    display:flex;align-items:center;padding-left:14px;gap:10px;
  }
  .back-band .wordmark{font-weight:300;font-size:22px;letter-spacing:1px;color:var(--text-grey)}
  .back-band .address{font-size:4.6px;line-height:5.6px;color:#555}
</style>
</head>
<body>

  <section class="panel front-cover" aria-label="Front cover">
    <svg class="art" width="260" height="347" viewBox="0 0 260 347">
      <path d="M0 0 H124 Q40 28 0 118 Z" fill="var(--orange-deep)"/>
      <path d="M0 0 H70 Q20 20 0 60 Z" fill="var(--orange)" opacity=".55"/>
      <path d="M260 252 Q150 270 92 347 H260 Z" fill="var(--teal)"/>
      <path d="M260 290 Q190 300 150 347 H260 Z" fill="var(--blue)" opacity=".7"/>
      <line x1="82" y1="166" x2="82" y2="236" stroke="var(--blue)" stroke-width="1"/>
      <line x1="176" y1="220" x2="176" y2="270" stroke="var(--blue)" stroke-width="1"/>
      <path d="M173 266 L176 271 L179 266" fill="none" stroke="var(--blue)" stroke-width="1"/>
    </svg>
    <div class="wordmark">HALVERN IT</div>
    <div class="product-band">
      <div class="products" role="img" aria-label="Product photos: rack servers, a WiFi access point and a network circuit board"></div>
    </div>
  </section>

  <section class="panel inside-left" aria-label="Inside left panel">
    <div class="pocket pocket-left"><div class="wordmark">HALVERN IT</div></div>
  </section>

  <section class="panel inside-right" aria-label="Inside right panel">
    <div class="pocket pocket-right">
      <div class="business-card">
        <div class="card-name">HALVERN IT</div>
        <div class="card-lines">480 Seabright Ave. Suite 210<br>Lantern Bay, CA 90000<br>555-014-2260<br>www.halvernit.com</div>
      </div>
    </div>
  </section>

  <section class="panel back-cover" aria-label="Back cover">
    <svg class="art" width="260" height="347" viewBox="0 0 260 347">
      <path d="M150 0 Q250 60 260 170 V0 Z" fill="var(--blue-light)" opacity=".45"/>
      <path d="M0 262 Q120 238 260 250 V268 H0 Z" fill="var(--blue-light)" opacity=".5"/>
      <path d="M150 347 Q220 320 260 300 V347 Z" fill="var(--blue-light)" opacity=".45"/>
    </svg>
    <div class="back-band">
      <div class="wordmark">HALVERN IT</div>
      <div class="address">Corporate Headquarters<br>480 Seabright Ave. Suite 210<br>Lantern Bay, CA 90000<br>555-014-2260<br>www.halvernit.com</div>
    </div>
  </section>

</body>
</html>
```